Business card for Bio pharmaceutical company

Hello,
We are a bio pharmaceutical contract manufacturing company in Brisbane, Australia. Can you please create a new business card design. Please go to our website for colours http://www.veltromedix.com.au.
On the back can you include the cartoon mascot Tobi Warn and the tagline
"A Global Biopharmaceutical Contract Development Manufacturing Company"
Target Market(s)
Biotechnology
Industry/Entity Type
Pharmaceutical
Contact Information for Business Card
Karen Holbrooke
Business Development Manager
karen.holbrooke@veltromedix.com.au
1937 Mulgrave Street Kelby Queesnland 4076 Australia
T: +61 7 3591 6042
M +61 427 516 908
F +61 7 3648 2095
www.veltromedix.com.au

```html
<!DOCTYPE html>
<html lang="en">
<head>
<meta charset="utf-8">
<title>VeltroMedix Business Card</title>
<link rel="stylesheet" href="https://fonts.googleapis.com/css2?family=Lato:wght@400;700;900&display=swap">
<style>
  :root {
    --stage: #e9e4de;
    --card-white: #ffffff;
    --brand-blue: #1b8fd0;
    --brand-navy: #17406b;
    --ink: #2b2b2b;
    --rule: #7cc3ea;
    --lime: #c9dc2c;
    --mascot-light: #a9d8f2;
    --mascot-mid: #5fb4e6;
  }
  * { margin: 0; padding: 0; box-sizing: border-box; }
  html, body { width: 1200px; height: 900px; overflow: hidden; }
  body {
    background: var(--stage);
    font-family: "Lato", Arial, sans-serif;
    position: relative;
  }
  .card {
    position: absolute;
    top: 295px;
    width: 540px;
    height: 310px;
    overflow: hidden;
    box-shadow: 0 6px 18px rgba(0,0,0,0.18);
  }
  .card--front { left: 45px; background: var(--card-white); }
  .card--back { left: 615px; background: var(--brand-blue); }

  .brand {
    position: absolute; left: 30px; top: 92px;
    display: flex; align-items: center; gap: 8px;
  }
  .brand__mark { width: 14px; height: 14px; background: var(--brand-blue); }
  .brand__name { font-size: 30px; font-weight: 700; color: var(--brand-navy); letter-spacing: -0.5px; }

  .holder { position: absolute; right: 30px; top: 32px; text-align: right; }
  .holder__name { font-size: 23px; font-weight: 700; color: var(--brand-blue); letter-spacing: 0.5px; }
  .holder__title { font-size: 13px; font-weight: 900; color: var(--ink); margin-top: 2px; }

  .divider { position: absolute; left: 30px; right: 30px; top: 130px; height: 1px; background: var(--rule); }

  .contacts { position: absolute; left: 30px; top: 150px; list-style: none; }
  .contacts__item {
    display: flex; align-items: center; gap: 8px;
    font-size: 16px; line-height: 22px; color: var(--ink);
  }
  .contacts__icon { width: 14px; height: 14px; flex: none; fill: var(--brand-blue); }

  .front-band { position: absolute; left: 0; bottom: 0; width: 540px; height: 40px; }

  .tagline {
    position: absolute; left: 30px; bottom: 40px;
    color: #fff; font-size: 25px; line-height: 29px; font-weight: 400;
    text-shadow: 0 1px 2px rgba(0,0,0,0.25);
  }
  .mascot {
    position: absolute; right: 40px; top: 30px; width: 130px; height: 170px;
    border-radius: 12px;
    background: linear-gradient(160deg, var(--mascot-light), var(--mascot-mid));
  }
  .website {
    position: absolute; right: 30px; top: 214px;
    font-size: 16px; font-weight: 700; color: #fff;
  }
  .website__domain { color: var(--lime); }
</style>
</head>
<body>

<section class="card card--front">
  <div class="brand">
    <span class="brand__mark"></span>
    <span class="brand__name">VeltroMedix</span>
  </div>

  <div class="holder">
    <div class="holder__name">Karen Holbrooke</div>
    <div class="holder__title">Business Development Manager</div>
  </div>

  <div class="divider"></div>

  <ul class="contacts">
    <li class="contacts__item">
      <svg class="contacts__icon" viewBox="0 0 16 16"><path d="M2 5c0-2 2-3 6-3s6 1 6 3v1h-3V5H5v1H2z"/><rect x="3" y="8" width="10" height="6" rx="1"/></svg>
      +61 7 3591 6042
    </li>
    <li class="contacts__item">
      <svg class="contacts__icon" viewBox="0 0 16 16"><path d="M4 1h8v14H4z M5.5 3v9h5V3z" fill-rule="evenodd"/></svg>
      +61 427 516 908
    </li>
    <li class="contacts__item">
      <svg class="contacts__icon" viewBox="0 0 16 16"><rect x="4" y="1" width="8" height="5"/><rect x="1" y="6" width="14" height="6" rx="1"/><rect x="4" y="11" width="8" height="4"/></svg>
      +61 7 3648 2095
    </li>
    <li class="contacts__item">
      <svg class="contacts__icon" viewBox="0 0 16 16"><path d="M1 3h14v10H1z"/><path d="M1 3l7 6 7-6" fill="none" stroke="#fff" stroke-width="1.2"/></svg>
      karen.holbrooke@veltromedix.com.au
    </li>
    <li class="contacts__item">
      <svg class="contacts__icon" viewBox="0 0 16 16"><path d="M8 1a5 5 0 0 0-5 5c0 4 5 9 5 9s5-5 5-9a5 5 0 0 0-5-5zm0 3a2 2 0 1 1 0 4 2 2 0 0 1 0-4z" fill-rule="evenodd"/></svg>
      1937 Mulgrave Street Kelby Queesnland 4076 Australia
    </li>
  </ul>

  <svg class="front-band" viewBox="0 0 540 40" preserveAspectRatio="none">
    <polygon points="220,40 236,12 540,0 540,40" fill="var(--brand-blue)"/>
  </svg>
</section>

<section class="card card--back">
  <div class="mascot" role="img" aria-label="Cartoon mascot Tobi Warn, a friendly blue microbe character, with the brand tagline beneath"></div>
  <div class="website">www.<span class="website__domain">veltromedix</span>.com.au</div>
  <p class="tagline">A Global<br>Biopharmaceutical<br>Contract Development<br>Manufacturing Company</p>
</section>

</body>
</html>
```